Vantor - Adventurous, Fun, Exciting, Social Fitness Club needs a Webpage with attitude!

Vantor... we're a fun, social, outdoor fitness club that needs not just a homepage designed for our website, but in the process a "personality" for our unique, innovative and cheeky brand.
We pride ourselves on getting our members outdoors trying new, exciting physical activities in an effort to find joy in an active lifestyle, and sharing that experience with other like minded people. We offer:
- Personal Training (1-on-1 Fitness Training)
- Group Fitness Classes (Boxing, Pilates, etc)
- Boot Camps (Military Style - Sandbags, Ropes, Tyres, etc)
- Events (Fun Runs, Triathlons, Ocean Swims, Treks, etc)
- Adventures(Machu Picchu Trek, Rock Climbing, Kayaking, etc)
Our tag line is 'No Judgements. No Limits!' The homepage should be exciting, adventurous and innovative, illustrating the values of our brand: possibility, thirst for life, personal accomplishment & freedom. It should be fun, friendly & inviting.
A few of our key benefits to members are:
- No Boring Workouts
- No Joining Fees or Long Term Contracts
- Results Guaranteed
The links below should give you a rough idea of the sort of "feel" we're after (vibrant, active, adventurous ).
http://www.pupiljourneys.com.au/
http://www.layoutgoblin.com/website-templates/31924.html
http://www.layoutgoblin.com/website-templates/32751.html
http://www.pivel.com/
Target Market(s)
Real, Everyday People - Men & Women (30:70) aged mainly between 21-40, who want a more exciting and enjoyable fitness experience than your typical gym offers.
Industry/Entity Type
Fitness
Requirements
Must have
- Strong, uplifting and motivating images of people enjoying fitness/physical activities outdoors

```html
<!DOCTYPE html>
<html lang="en">
<head>
<meta charset="utf-8">
<title>Vantor – Adventure Fitness Club</title>
<link href="https://fonts.googleapis.com/css2?family=Anton&family=Arimo:wght@400&family=Roboto+Condensed:ital,wght@0,400;0,700;1,400;1,700&display=swap" rel="stylesheet">
<style>
  :root{
    --red:#e04a25;
    --red-dark:#c9310f;
    --red-deep:#b42a0d;
    --yellow:#f5c21a;
    --ink:#111;
    --white:#fff;
    --paper:rgba(255,255,255,.9);
    --rock-1:#efe9e1;
    --rock-2:#d9d2c8;
  }
  *{box-sizing:border-box;margin:0;padding:0}
  html,body{width:1200px;height:1005px;overflow:hidden}
  body{position:relative;font-family:"Roboto Condensed",sans-serif;color:var(--ink)}
  .abs{position:absolute}
  .backdrop{inset:0;background:linear-gradient(110deg,var(--rock-1) 0%,var(--rock-2) 35%,#e6e0d8 60%,#cfc8bf 100%)}
  .frame{inset:0}
  .page{left:136px;top:137px;width:928px;height:868px;background:var(--paper)}
  .header{left:136px;top:68px;width:928px;height:69px;background:var(--red)}
  .nav-marker{left:546px;top:68px}
  .brand{left:160px;top:72px;display:flex;align-items:center;gap:10px;font-weight:700;font-size:46px;color:var(--yellow);letter-spacing:1px}
  .brand-dot{width:16px;height:16px;border-radius:50%;background:var(--ink)}
  .main-nav{left:545px;top:95px;display:flex;font-size:15px;font-weight:700;color:var(--white)}
  .main-nav a,.foot-nav a{color:inherit;text-decoration:none;position:absolute;white-space:nowrap}
  .phone{left:843px;top:12px;font-size:19px}
  .social{top:15px;width:15px;height:15px;background:#3b5998;border-radius:2px}
  .social.video{background:#c8262a}
  .util-nav{top:39px;font-size:12px;font-weight:700;color:var(--red)}
  .hero-photo{left:136px;top:138px;width:690px;height:304px;background:linear-gradient(160deg,#aecde0 0%,#4e7fb0 40%,#22528c 75%,#c7a12a 100%)}
  .hero-copy{left:136px;top:173px;width:485px;height:228px;background:rgba(80,110,160,.55);padding:20px 0 0 52px;color:var(--white)}
  .hero-copy h1{font-size:43px;line-height:54px;font-weight:700}
  .hero-copy p{font-size:11.5px;line-height:16px;margin-top:14px;width:420px}
  .hero-copy .more{display:inline-block;margin-top:14px;font-size:12px;font-weight:700;color:var(--white)}
  .signup{left:786px;top:138px}
  .signup-body{left:802px;top:152px;color:var(--white)}
  .signup-body h2{font-size:20px;font-weight:700;white-space:nowrap}
  .signup-body .value{font-size:43px;font-weight:700;margin:2px 0 0 28px;line-height:48px}
  .signup-body ul{list-style:none;margin:6px 0 0 28px;font-size:11.5px;font-weight:700;line-height:22.5px}
  .field-label{left:830px;font-size:12px;font-weight:700;color:var(--white)}
  .field{left:875px;width:146px;height:22px;background:var(--white);border:0}
  .join{left:875px;top:386px;width:146px;height:41px;background:var(--red);color:var(--white);font-size:22px;display:flex;align-items:center;justify-content:center}
  .service-img{height:112px}
  .service{width:260px;text-align:center}
  .service h3{font-size:21px;font-weight:400}
  .service p{font-family:Arimo,sans-serif;font-size:12.5px;margin-top:3px}
  .service .foot{position:relative;height:20px;margin-top:4px}
  .service .price{position:absolute;font-weight:700;font-size:14.5px;color:var(--red)}
  .service .rm{position:absolute;font-style:italic;font-weight:700;font-size:10.5px;color:var(--red);top:3px}
  .headline{left:190px;top:618px;font-family:Anton,sans-serif;font-size:62px;letter-spacing:1px;transform:scaleY(1.35);transform-origin:left top;white-space:nowrap}
  .intro{left:190px;top:744px;width:475px;font-family:Arimo,sans-serif;font-size:12px;line-height:18.75px}
  .runner{left:683px;top:637px;width:299px;height:198px;background:linear-gradient(180deg,#3a6fb5 0%,#6e98c8 55%,#4f7a2e 70%,#7b9b3c 100%)}
  .rule{left:190px;top:896px;width:822px;height:3px;background:var(--red)}
  .foot-nav{top:913px;font-size:15px;font-weight:700;color:var(--ink)}
  .copyright{left:0;width:1195px;top:946px;text-align:center;font-size:10px;color:var(--red)}
</style>
</head>
<body>
  <div class="abs backdrop" role="img" aria-label="Soft rock cliff with a climber in the background"></div>

  <svg class="abs frame" width="1200" height="1005" viewBox="0 0 1200 1005" aria-hidden="true">
    <polygon points="80,0 764,0 619,39 300,22" fill="var(--yellow)"/>
    <polygon points="136,68 109,459 166,548 166,137" fill="var(--red-dark)"/>
    <polygon points="1064,137 1097,816 1064,923" fill="var(--red-dark)"/>
  </svg>

  <div class="abs page"></div>
  <div class="abs header"></div>
  <svg class="abs nav-marker" width="36" height="19" aria-hidden="true"><polygon points="0,0 36,0 18,18" fill="var(--red-deep)"/></svg>

  <div class="abs brand"><span class="brand-dot"></span>VANTOR</div>

  <div class="abs phone">1300 555 019</div>
  <span class="abs social" style="left:965px" aria-label="Social page"></span>
  <span class="abs social video" style="left:994px" aria-label="Video channel"></span>
  <a class="abs util-nav" style="left:802px">TIMETABLE</a>
  <a class="abs util-nav" style="left:877px">CLUB LOCATIONS</a>
  <a class="abs util-nav" style="left:981px">LOGIN</a>

  <nav class="abs main-nav">
    <a style="left:0">HOME</a>
    <a style="left:67px">ABOUT US</a>
    <a style="left:154px">FITNESS</a>
    <a style="left:232px">EVENTS &amp; ADVENTURES</a>
    <a style="left:395px">CONTACT US</a>
  </nav>

  <div class="abs hero-photo" role="img" aria-label="Photo of a kayaker paddling on open sea"></div>
  <div class="abs hero-copy">
    <h1>No Judgements.<br>No Limits!</h1>
    <p>After an initial consultation to see if Stride Fitness is the right fit for you, we will assess your current physical health status. We will also discuss your nutritional habits in detail to assure you will make the most of your training with Stride Fitness.</p>
    <a class="more" style="text-decoration:underline">Read more</a>
  </div>

  <svg class="abs signup" width="278" height="304" aria-hidden="true"><polygon points="0,0 278,0 278,304 35,304" fill="var(--red-dark)"/></svg>
  <div class="abs signup-body">
    <h2>FREE MEMBERSHIP, JOIN US</h2>
    <div class="value">Valued $65</div>
    <ul>
      <li>Monthly E-news hints, tips and advice</li>
      <li>Vip invites events &amp; adventures</li>
      <li>Special Member only offers</li>
      <li>Discount card to 20+ providers</li>
    </ul>
  </div>
  <label class="abs field-label" style="top:333px">Name</label>
  <input class="abs field" style="top:330px" aria-label="Name">
  <label class="abs field-label" style="top:363px">Email</label>
  <input class="abs field" style="top:358px" aria-label="Email">
  <div class="abs join">Join Us</div>

  <div class="abs service-img" style="left:242px;top:422px;width:152px;background:linear-gradient(135deg,#5fd4a8,#8a8a8a)" role="img" aria-label="Resistance band with handles"></div>
  <div class="abs service-img" style="left:514px;top:422px;width:169px;background:linear-gradient(180deg,#e8e6e1,#e2652b 55%,#4c5a45)" role="img" aria-label="Camping tent"></div>
  <div class="abs service-img" style="left:806px;top:412px;width:132px;height:122px;background:linear-gradient(160deg,#e0322f,#9c1414)" role="img" aria-label="Red boxing glove"></div>

  <div class="abs service" style="left:179px;top:536px">
    <h3>Personal Training</h3>
    <p>Free Initial Consult and 1 on 1 session</p>
    <div class="foot"><span class="price" style="left:56px">(Valued $80)</span><span class="rm" style="left:162px">read more</span></div>
  </div>
  <div class="abs service" style="left:467px;top:536px">
    <h3>Boot Camps</h3>
    <p>Intro pass $25, 7 days unlimited classes</p>
    <div class="foot"><span class="rm" style="left:110px">read more</span></div>
  </div>
  <div class="abs service" style="left:754px;top:536px">
    <h3>Group Fitness</h3>
    <p>Starts soon, #s limited</p>
    <div class="foot"><span class="price" style="left:72px">Enlist</span><span class="rm" style="left:136px">read more</span></div>
  </div>

  <div class="abs headline">FITNESS FOR LIFE</div>
  <p class="abs intro">Sed ut perspiciatis unde omnis iste natus error sit voluptatem accusantium doloremque laudantium, totam rem aperiam, eaque ipsa quae ab illo inventore veritatis et quasi architecto beatae vitae dicta sunt explicabo. Nemo enim ipsam voluptatem quia voluptas sit aspernatur aut odit aut fugit, sed quia consequuntur magni dolores eos qui ratione voluptatem sequi nesciunt. Neque porro quisquam est, qui dolorem ipsum quia dolor sit amet, consectetur.</p>
  <div class="abs runner" role="img" aria-label="Photo of a woman jogging on a grassy coastal headland"></div>

  <div class="abs rule"></div>
  <nav class="abs foot-nav" style="left:363px">
    <a style="left:0">HOME</a>
    <a style="left:68px">ABOUT US</a>
    <a style="left:155px">FITNESS</a>
    <a style="left:232px">EVENTS &amp; ADVENTURES</a>
    <a style="left:395px">CONTACT US</a>
  </nav>
  <div class="abs copyright">copyright 2011 - Vantor.com - All rights reserved</div>
</body>
</html>
```